Verimo Cleaning Company Flyer

Hi, We need an A4 flyer design for our cleaning company, focusing on dry carpet cleaning I attached our catalogue to give some idea. In addition, our websites can provide more information. Our Services:-General Cleaning Carry out heavy cleansing tasks and special projects. Clean, stock and supply designated facility areas (dusting, sweeping, vacuuming, mopping, cleaning ceiling vents, restroom cleaning etc).Using electrically powered scrubbing and polishing machines to burnish, scrub, polish and spray clean floors. Window Cleaning Regular, Reliable Window Cleaning.Hard To Reach Windows.Single 7 Multi-Storey.Frames and Glass Cleaned.Floor Cleaning Cleaning Marble Cleaning & Polishing.Tile & Grout Cleaning.Hardwood Floors Services.Vinyl Floors.The PELKA Dry Extraction Carpet Cleaning System uses environmentally preferred, Amber Crest Certified cleaning products that deep cleans your carpets and textured hard floors quickly and easily.

Target Market(s)

Commercial Cleaning residential Cleaning Hotel cleaning

Industry/Entity Type

Cleaning Service

Contact Information for Business Card

Tariq Hamdan Al-Saeedi Gm
Derek Olmo Marketing Manger

Font styles to use
Serif
Sans Serif

Colors
0355a3
3176b5
85acd3
cee9f5
85cae6
34a6d7
0592cd

```html
<!DOCTYPE html>
<html lang="en">
<head>
<meta charset="utf-8">
<title>Verimo Cleaning Company Flyer</title>
<link href="https://fonts.googleapis.com/css2?family=Montserrat:wght@400;600;700;800&family=Merriweather:ital,wght@0,400;0,700;1,400&display=swap" rel="stylesheet">
<style>
:root{
  --navy:#0355a3;
  --blue:#3176b5;
  --sky:#85acd3;
  --ice:#cee9f5;
  --aqua:#85cae6;
  --cyan:#34a6d7;
  --azure:#0592cd;
  --deep:#0a2f6b;
  --ink:#33475b;
  --white:#ffffff;
}
*{margin:0;padding:0;box-sizing:border-box}
html,body{width:893px;height:1200px;overflow:hidden;background:#fff}
.flyer{position:relative;width:893px;height:1200px;background:var(--white);font-family:'Montserrat',sans-serif;color:var(--ink);overflow:hidden}
.brand{position:absolute;left:60px;top:48px;display:flex;align-items:center;gap:14px}
.brand-dot{width:54px;height:54px;border-radius:50%;background:var(--azure)}
.brand-name{font-family:'Merriweather',serif;font-weight:700;font-size:44px;color:var(--navy);line-height:1}
.brand-sub{font-family:'Merriweather',serif;font-weight:700;font-size:22px;color:var(--navy);margin-top:4px}
.hero-photo{position:absolute;right:0;top:0;width:440px;height:345px;background:linear-gradient(135deg,#c9a27a,#8d6b4c 55%,#e8e2dc)}
.hero-band{position:absolute;left:0;top:150px;width:893px;height:240px}
.headline{position:absolute;left:60px;top:205px;width:400px;font-weight:800;font-size:27px;line-height:1.25;color:var(--white);text-transform:uppercase}
.about{position:absolute;left:60px;top:415px;width:370px}
.section-title{font-family:'Merriweather',serif;font-weight:700;font-size:28px;color:var(--navy);text-align:center;position:relative;padding-bottom:12px}
.section-title::after{content:"";position:absolute;left:50%;bottom:0;width:120px;height:3px;margin-left:-60px;background:var(--cyan)}
.about p{font-size:12.5px;line-height:1.55;margin-top:18px;font-style:italic;font-family:'Merriweather',serif;color:var(--ink)}
.machines{position:absolute;left:60px;top:700px;width:370px;height:170px;background:linear-gradient(180deg,#f3f6fa,#b9c4d2);border-radius:6px}
.service-photo{position:absolute;right:60px;top:395px;width:360px;height:230px;background:linear-gradient(135deg,#8a5a33,#c89a6c 50%,#2f3e58);border:6px solid var(--white);box-shadow:0 0 0 2px var(--aqua)}
.services{position:absolute;right:60px;top:645px;width:360px}
.services .section-title{text-align:left}
.services .section-title::after{left:0;margin-left:0}
.services p{font-size:12px;line-height:1.45;margin-top:12px;color:var(--ink)}
.services strong{color:var(--navy)}
.welcome{position:absolute;left:60px;top:915px;width:390px;text-align:center}
.welcome h2{font-weight:800;font-size:25px;line-height:1.2;color:var(--navy);text-transform:uppercase}
.web{margin-top:12px;font-weight:700;font-size:22px;color:var(--azure)}
.phone-band{position:absolute;left:0;top:1035px;width:480px;height:66px;background:var(--navy);border-radius:0 40px 40px 0;display:flex;align-items:center;padding-left:48px;gap:14px}
.phone-band svg{width:34px;height:34px;flex-shrink:0}
.phone-label{font-size:10px;color:var(--ice);line-height:1.3;white-space:nowrap}
.phone-number{font-weight:800;font-size:27px;color:var(--white);white-space:nowrap}
.partner{position:absolute;right:60px;top:945px;width:360px;display:flex;gap:16px;align-items:flex-start}
.partner-mark{display:flex;align-items:center;gap:10px;flex-shrink:0;width:150px}
.partner-square{width:20px;height:20px;background:var(--azure)}
.partner-name{font-weight:800;font-size:36px;color:var(--navy);line-height:1}
.partner p{font-size:11px;line-height:1.45;color:var(--ink)}
.footer{position:absolute;left:0;bottom:0;width:893px;height:56px;background:linear-gradient(90deg,var(--deep),var(--navy));display:flex;justify-content:space-between;align-items:center;padding:0 60px;color:var(--white);font-size:14px;font-weight:600}
.footer-accent{position:absolute;left:0;bottom:56px;width:893px;height:8px;background:var(--cyan)}
</style>
</head>
<body>
<div class="flyer">
  <div class="hero-photo" role="img" aria-label="Photo of a technician in a dark uniform cleaning carpet with a dry extraction machine beside a wooden door"></div>
  <svg class="hero-band" viewBox="0 0 893 240" preserveAspectRatio="none">
    <path d="M0 40 Q230 20 480 60 L480 60 Q520 190 440 240 L0 240 Z" fill="#85cae6"/>
    <path d="M0 52 Q220 34 460 70 Q495 180 420 232 L0 232 Z" fill="#0355a3"/>
    <path d="M0 200 Q300 260 893 180 L893 240 L0 240 Z" fill="#ffffff"/>
    <path d="M0 206 Q300 262 893 186" fill="none" stroke="#34a6d7" stroke-width="4"/>
  </svg>

  <div class="brand">
    <div class="brand-dot"></div>
    <div>
      <div class="brand-name">Verimo</div>
      <div class="brand-sub">Cleaning</div>
    </div>
  </div>

  <h1 class="headline">For big jobs, tough jobs and regular maintaince use!</h1>

  <section class="about">
    <h2 class="section-title">About Us</h2>
    <p>With over 25 years in operation, Verimo Cleaning Co. has established itself as a successful business in the cleaning industry and has accumulated expert knowledge on cleaning processes and procedures to ensure your premises are maintained to the highest standards. Our staff are chosen meticulously through rigorous interview and employment procedures so that you can feel comfortable leaving your property and assets in safe, secure and professional hands. We are the official dealer / distributor of PELKA Dry Extraction Carpet Cleaning System in Qatar.</p>
  </section>
  <div class="machines" role="img" aria-label="Product photo of dry extraction carpet cleaning machines and cleaning compound tubs"></div>

  <div class="service-photo" role="img" aria-label="Photo of a technician vacuuming a carpet in a hallway"></div>
  <section class="services">
    <h2 class="section-title">OUR SERVICES</h2>
    <p>General Cleaning Carry out heavy cleansing tasks and special projects. Clean, stock and supply designated facility areas <strong>(Dusting, Sweeping, Vacuuming, Mopping, Cleaning Ceiling vents, Restroom cleaning etc.)</strong></p>
    <p>Using electrically powered scrubbing and polishing machines to burnish, scrub, polish and spray clean floors. Window Cleaning Regular, Reliable Window Cleaning. Hard To Reach Windows. Single &amp; Multi-Storey. Frames and Glass Cleaned. Floor Cleaning Marble Cleaning &amp; Polishing. Tile &amp; Grout Cleaning. Hardwood Floors Services. Vinyl Floors.</p>
  </section>

  <section class="welcome">
    <h2>Welcome visitors &amp;<br>announce promotions</h2>
    <div class="web">www.verimocleaning.com</div>
  </section>
  <div class="phone-band">
    <svg viewBox="0 0 24 24"><circle cx="12" cy="12" r="12" fill="#34a6d7"/><path d="M8.2 6.5l1.8-.4 1.1 2.7-1.3 1a7 7 0 003.4 3.4l1-1.3 2.7 1.1-.4 1.8c-.2.6-.8.9-1.4.8A9.5 9.5 0 017.4 7.9c-.1-.6.2-1.2.8-1.4z" fill="#fff"/></svg>
    <div class="phone-label">Contact us to know more<br>about our services</div>
    <div class="phone-number">+974 5550 1234</div>
  </div>

  <section class="partner">
    <div class="partner-mark">
      <div class="partner-square"></div>
      <div class="partner-name">PELKA</div>
    </div>
    <p>The PELKA Dry Extraction Carpet Cleaning System uses environmentally preferred, Amber Crest Certified cleaning products that deep cleans your carpets and textured hard floors quickly and easily.</p>
  </section>

  <div class="footer-accent"></div>
  <footer class="footer">
    <span>info@verimocleaning.com</span>
    <span>www.verimocleaning.com</span>
  </footer>
</div>
</body>
</html>
```